Pavlex New Stunning Brochure Design

What we do: "We design tailor-made solutions to fit your Human Capital and Industrial Cleaning needs, ensuring peace of mind."
We are in the process of having new presentation folders printed and need assistance with the layout. The folders are used to place presentation documents, quotes, costings, etc. in the folder to hand to clients / prospective clients. Under the “reference material section”, you’ll find a Word Document with the outline of the contents. Although we have four different pages, we need to see the cohesion between the different pages…content flow… A3 fold to A4 with flap with slits for business card.
Aims and requirements:
• To “wow” the reader – first impressions last!
• 3D Logo and images / design
• Professional
• Hi-Tech
• Innovative
• Impressive
• Something new / completely different
• Focus on “tailor-made solutions” linked to innovation
Updates

Project Deadline Extended Reason: I have taken leave and will only be back on the 6th May. Thought I might give the designers more time then as I won't be in the office on the 29th to finalize the contest anyways! Happy Designing! Added Wednesday, April 22, 2015

Target Market(s)

The folders are used to place presentation documents, quotes, costings, etc. in the folder to hand to clients / prospective clients. Under the “reference material section”, you’ll find a Word Document with the outline of the contents.

Industry/Entity Type

Tailor

Requirements
Must have
• Although we have four different pages, we need to see the cohesion between the different pages…content flow…
• Aims and requirements:
• • To “wow” the reader – first impressions last!
• • 3D Logo and images / design
• • Professional
• • Hi-Tech
• • Innovative
• • Impressive
• • Something new / completely different
• • Focus on “tailor-made solutions” linked to innovation
• The folder must be print ready with the following specifications:
• Description – A3 fold to A4 Company profiles printed in full colour both sides plus gloss uv varnish front only, scored, die –cut, flap glued with 2 business cards slits.
• Size - 305 mm x 214 mm (A4 insert should fit inside the folder and flap.
• Stock - Verrin Duo Lumo Gloss, White, 250 gsm

```html
<!DOCTYPE html>
<html lang="en">
<head>
<meta charset="utf-8">
<title>Pavlex Presentation Folder – Inside Spread</title>
<link rel="stylesheet" href="https://fonts.googleapis.com/css2?family=Open+Sans:ital,wght@0,300;0,400;0,600;0,700;1,300;1,400&display=swap">
<style>
  :root {
    --stage: #d8d5d1;
    --paper-light: #eceef0;
    --paper-mid: #d5d9de;
    --navy: #1c4f7c;
    --navy-deep: #123a5e;
    --blue: #1f64a0;
    --blue-soft: #3b7fba;
    --ink: #2a3440;
    --ink-soft: #56606b;
    --white: #ffffff;
    --card-white: #f4f4f2;
    --quote: #6d747c;
  }
  * { box-sizing: border-box; margin: 0; padding: 0; }
  html, body {
    width: 1200px; height: 820px; overflow: hidden;
    background: var(--stage);
    font-family: "Open Sans", Arial, sans-serif;
    color: var(--ink);
  }
  .folder {
    position: absolute; left: 60px; top: 30px;
    width: 1080px; height: 760px;
    display: flex;
    box-shadow: 0 6px 18px rgba(0,0,0,.18);
  }
  .panel { position: relative; width: 540px; height: 760px; overflow: hidden; }

  /* Left panel */
  .panel--left {
    background: linear-gradient(180deg, var(--paper-light) 0%, var(--paper-mid) 70%, #c9ced5 100%);
    border-top: 4px solid var(--navy);
  }
  .vision { position: absolute; left: 30px; top: 24px; }
  .vision__eyebrow {
    position: absolute; left: 200px; top: 2px;
    font-size: 10px; color: var(--ink-soft); letter-spacing: .5px;
  }
  .vision__title {
    margin-top: 12px;
    font-size: 40px; font-weight: 300; color: var(--navy); letter-spacing: -.5px;
  }
  .vision__title strong { font-weight: 700; }

  .benefits {
    position: absolute; left: 24px; top: 100px;
    width: 492px; height: 600px;
    background: var(--navy);
    border-radius: 34px 14px 14px 14px;
    padding: 14px;
  }
  .benefits__card {
    width: 100%; height: 100%;
    background: var(--card-white);
    border-radius: 26px 8px 8px 8px;
    padding: 22px 24px 0 24px;
  }
  .benefits__title {
    font-size: 22px; font-weight: 400; color: var(--navy-deep);
    margin-bottom: 12px;
  }
  .benefits__list { list-style: none; }
  .benefit {
    display: flex; gap: 10px; align-items: flex-start;
    margin-bottom: 8px;
  }
  .benefit__tick { flex: 0 0 16px; margin-top: 1px; }
  .benefit__name {
    font-size: 11.5px; font-weight: 700; color: var(--navy-deep);
    text-transform: uppercase; line-height: 1.25;
  }
  .benefit__desc { font-size: 11px; color: var(--ink-soft); line-height: 1.3; }

  /* Right panel */
  .panel--right {
    background: linear-gradient(180deg, #dfe2e6 0%, #d6dade 100%);
    border-top: 4px solid var(--navy);
  }
  .hero-photo {
    position: absolute; left: 0; top: 80px; width: 540px; height: 390px;
    background:
      radial-gradient(ellipse at 75% 45%, rgba(240,190,140,.75) 0%, rgba(240,190,140,0) 40%),
      linear-gradient(120deg, #8a96a6 0%, #4a5a70 45%, #2d3a4e 100%);
  }
  .growth-line { position: absolute; left: 0; top: 120px; }
  .quote {
    position: absolute; left: 40px; top: 488px; width: 470px;
    font-size: 15px; font-style: italic; font-weight: 300;
    color: var(--quote); line-height: 1.4;
  }
  .quote__source { display: block; text-align: center; font-style: normal; font-size: 13px; margin-top: 2px; }

  .card-flap {
    position: absolute; left: 0; top: 590px; width: 540px; height: 170px;
    background: linear-gradient(180deg, var(--blue) 0%, var(--navy) 100%);
    border-radius: 10px 10px 0 0;
  }
  .contact {
    position: absolute; font-size: 12px; color: var(--white);
    display: flex; flex-direction: column; gap: 6px;
  }
  .contact__row { display: flex; align-items: center; gap: 8px; }
  .contact__dot {
    width: 14px; height: 14px; border-radius: 50%;
    background: rgba(255,255,255,.85);
  }
  .contact__at { font-size: 18px; font-weight: 300; width: 14px; line-height: 1; }
  .contact--web { left: 36px; top: 14px; }
  .contact--mail { left: 300px; top: 14px; }

  .business-card {
    position: absolute; width: 210px; height: 104px;
    background: var(--white);
    clip-path: polygon(10% 0, 90% 0, 100% 30%, 100% 100%, 0 100%, 0 30%);
    display: flex; align-items: center; justify-content: center; gap: 8px;
  }
  .business-card--one { left: 30px; top: 62px; }
  .business-card--two { left: 300px; top: 62px; }
  .business-card__mark { width: 12px; height: 12px; border-radius: 50%; background: var(--navy); }
  .business-card__name {
    font-size: 14px; font-weight: 700; color: var(--navy-deep); letter-spacing: 1.5px;
  }
</style>
</head>
<body>
  <main class="folder">
    <section class="panel panel--left">
      <header class="vision">
        <span class="vision__eyebrow">Our Vision</span>
        <h1 class="vision__title">Driven by <strong>your success</strong></h1>
      </header>

      <div class="benefits">
        <div class="benefits__card">
          <h2 class="benefits__title">Why our clients choose Pavlex?</h2>
          <ul class="benefits__list">
            <li class="benefit"><svg class="benefit__tick" viewBox="0 0 16 16" width="16" height="16"><circle cx="8" cy="8" r="7" fill="none" stroke="#1c4f7c" stroke-width="1.6"/><path d="M4.5 8.2l2.4 2.4 4.6-5" fill="none" stroke="#1c4f7c" stroke-width="1.8"/></svg><div><p class="benefit__name">Extremely efficient</p><p class="benefit__desc">Our front office becomes your back office</p></div></li>
            <li class="benefit"><svg class="benefit__tick" viewBox="0 0 16 16" width="16" height="16"><circle cx="8" cy="8" r="7" fill="none" stroke="#1c4f7c" stroke-width="1.6"/><path d="M4.5 8.2l2.4 2.4 4.6-5" fill="none" stroke="#1c4f7c" stroke-width="1.8"/></svg><div><p class="benefit__name">Highly effective</p><p class="benefit__desc">We get results; you can only manage what you measure</p></div></li>
            <li class="benefit"><svg class="benefit__tick" viewBox="0 0 16 16" width="16" height="16"><circle cx="8" cy="8" r="7" fill="none" stroke="#1c4f7c" stroke-width="1.6"/><path d="M4.5 8.2l2.4 2.4 4.6-5" fill="none" stroke="#1c4f7c" stroke-width="1.8"/></svg><div><p class="benefit__name">Supremely skilled staff</p><p class="benefit__desc">Matching your hire to retire requirements. No excuses</p></div></li>
            <li class="benefit"><svg class="benefit__tick" viewBox="0 0 16 16" width="16" height="16"><circle cx="8" cy="8" r="7" fill="none" stroke="#1c4f7c" stroke-width="1.6"/><path d="M4.5 8.2l2.4 2.4 4.6-5" fill="none" stroke="#1c4f7c" stroke-width="1.8"/></svg><div><p class="benefit__name">Rapid right fit recruiting</p><p class="benefit__desc">Great talent is hard to find – they are already working for us</p></div></li>
            <li class="benefit"><svg class="benefit__tick" viewBox="0 0 16 16" width="16" height="16"><circle cx="8" cy="8" r="7" fill="none" stroke="#1c4f7c" stroke-width="1.6"/><path d="M4.5 8.2l2.4 2.4 4.6-5" fill="none" stroke="#1c4f7c" stroke-width="1.8"/></svg><div><p class="benefit__name">Proven business solutions</p><p class="benefit__desc">Testimony of more than 450 satisfied clients since 1982</p></div></li>
            <li class="benefit"><svg class="benefit__tick" viewBox="0 0 16 16" width="16" height="16"><circle cx="8" cy="8" r="7" fill="none" stroke="#1c4f7c" stroke-width="1.6"/><path d="M4.5 8.2l2.4 2.4 4.6-5" fill="none" stroke="#1c4f7c" stroke-width="1.8"/></svg><div><p class="benefit__name">Exceptional cleaning with a difference</p><p class="benefit__desc">Cleaning is critical. A clean space is a safe place</p></div></li>
            <li class="benefit"><svg class="benefit__tick" viewBox="0 0 16 16" width="16" height="16"><circle cx="8" cy="8" r="7" fill="none" stroke="#1c4f7c" stroke-width="1.6"/><path d="M4.5 8.2l2.4 2.4 4.6-5" fill="none" stroke="#1c4f7c" stroke-width="1.8"/></svg><div><p class="benefit__name">Our labour and executive talent pool skill sets are vast</p><p class="benefit__desc">We supply your staffing and cleaning needs</p></div></li>
            <li class="benefit"><svg class="benefit__tick" viewBox="0 0 16 16" width="16" height="16"><circle cx="8" cy="8" r="7" fill="none" stroke="#1c4f7c" stroke-width="1.6"/><path d="M4.5 8.2l2.4 2.4 4.6-5" fill="none" stroke="#1c4f7c" stroke-width="1.8"/></svg><div><p class="benefit__name">Exceptional client satisfaction</p><p class="benefit__desc">98% and above since June 2012</p></div></li>
            <li class="benefit"><svg class="benefit__tick" viewBox="0 0 16 16" width="16" height="16"><circle cx="8" cy="8" r="7" fill="none" stroke="#1c4f7c" stroke-width="1.6"/><path d="M4.5 8.2l2.4 2.4 4.6-5" fill="none" stroke="#1c4f7c" stroke-width="1.8"/></svg><div><p class="benefit__name">Flexible</p><p class="benefit__desc">We offer custom cost &amp; compensation structure for your short medium and long term requirements</p></div></li>
            <li class="benefit"><svg class="benefit__tick" viewBox="0 0 16 16" width="16" height="16"><circle cx="8" cy="8" r="7" fill="none" stroke="#1c4f7c" stroke-width="1.6"/><path d="M4.5 8.2l2.4 2.4 4.6-5" fill="none" stroke="#1c4f7c" stroke-width="1.8"/></svg><div><p class="benefit__name">Spotless track record</p><p class="benefit__desc">No findings since 1982, and international accreditations</p></div></li>
            <li class="benefit"><svg class="benefit__tick" viewBox="0 0 16 16" width="16" height="16"><circle cx="8" cy="8" r="7" fill="none" stroke="#1c4f7c" stroke-width="1.6"/><path d="M4.5 8.2l2.4 2.4 4.6-5" fill="none" stroke="#1c4f7c" stroke-width="1.8"/></svg><div><p class="benefit__name">Timely payments</p><p class="benefit__desc">99.997% accuracy on-time payments</p></div></li>
          </ul>
        </div>
      </div>
    </section>

    <section class="panel panel--right">
      <div class="hero-photo" role="img" aria-label="Businessman in a suit reaching out and touching a rising growth chart"></div>
      <svg class="growth-line" width="540" height="80" viewBox="0 0 540 80" aria-hidden="true">
        <polyline points="0,38 130,38 250,30 370,28 480,48" fill="none" stroke="#ffffff" stroke-width="2" opacity=".85"/>
        <g fill="#4a5a70" stroke="#ffffff" stroke-width="2.5">
          <circle cx="130" cy="38" r="8"/>
          <circle cx="250" cy="30" r="8"/>
          <circle cx="370" cy="28" r="8"/>
          <circle cx="480" cy="48" r="8"/>
        </g>
      </svg>

      <blockquote class="quote">
        “Our deepest fear is not that we are inadequate. Our deepest fear is that we are powerful beyond measure.”
        <span class="quote__source">- Corvan Hale -</span>
      </blockquote>

      <div class="card-flap">
        <div class="contact contact--web">
          <div class="contact__row"><span class="contact__dot"></span><span>/pavlex</span></div>
          <div class="contact__row"><span class="contact__dot"></span><span>www.pavlex.com</span></div>
        </div>
        <div class="contact contact--mail">
          <div class="contact__row"><span class="contact__dot"></span><span>@pavlex</span></div>
          <div class="contact__row"><span class="contact__at">@</span><span>info@pavlex.com</span></div>
        </div>

        <div class="business-card business-card--one">
          <span class="business-card__mark"></span><span class="business-card__name">PAVLEX</span>
        </div>
        <div class="business-card business-card--two">
          <span class="business-card__mark"></span><span class="business-card__name">PAVLEX</span>
        </div>
      </div>
    </section>
  </main>
</body>
</html>
```